Harlow Grading LLC business card design

Excavation company business cards

Contact Information for Business Card

Harlow Grading LLC cell phone 208-471-9360 office phone 208-396-4815 harlowgradingllc@mailverde.net Driveways, site prep, retaining walls, septic systems, rock delivery

Colors

Designer to choose colors to be used in the design.

```html
<!DOCTYPE html>
<html lang="en">
<head>
<meta charset="utf-8">
<title>Harlow Grading LLC — Business Card</title>
<link rel="stylesheet" href="https://fonts.googleapis.com/css2?family=Montserrat:wght@700;800&family=Arimo:wght@400;700&display=swap">
<style>
  :root {
    --orange: #e8701f;
    --orange-light: #f58a3a;
    --grey: #6b6b6b;
    --white: #ffffff;
    --backdrop: #e6e6e6;
  }
  * { margin: 0; padding: 0; box-sizing: border-box; }
  html, body { width: 1200px; height: 1015px; overflow: hidden; }
  body {
    background: var(--backdrop);
    font-family: "Arimo", Arial, sans-serif;
    position: relative;
  }
  .card {
    position: absolute;
    left: 290px;
    width: 620px;
    height: 354px;
    overflow: hidden;
    box-shadow: 0 6px 18px rgba(0,0,0,0.18);
  }
  /* Front */
  .card-front { top: 90px; background: var(--white); }
  .brand {
    position: absolute;
    top: 110px; left: 0; right: 0;
    display: flex; align-items: center; justify-content: center; gap: 14px;
  }
  .brand-mark { width: 22px; height: 22px; background: var(--orange); }
  .brand-name {
    font-family: "Montserrat", sans-serif;
    font-weight: 800;
    font-size: 40px;
    letter-spacing: 1px;
    color: var(--orange);
  }
  .services-band {
    position: absolute;
    left: 0; right: 0; bottom: 26px;
    height: 34px;
  }
  .services-band svg { position: absolute; inset: 0; }
  .services-list {
    position: absolute;
    left: 70px; width: 480px; top: 0; height: 34px;
    display: flex; align-items: center; justify-content: center;
    color: var(--white); font-size: 13px; white-space: nowrap;
  }
  .services-list .sep { color: var(--orange-light); margin: 0 6px; }

  /* Back */
  .card-back { top: 520px; background: var(--orange); color: var(--white); }
  .machine-art {
    position: absolute;
    right: 0; top: 0;
    width: 300px; height: 354px;
    background: radial-gradient(ellipse at 55% 45%, var(--orange-light) 0%, rgba(245,138,58,0.55) 50%, rgba(232,112,31,0) 78%);
  }
  .contact { position: absolute; left: 44px; top: 44px; }
  .back-brand {
    font-family: "Montserrat", sans-serif;
    font-weight: 800; font-size: 44px; letter-spacing: 1px;
    line-height: 1; margin-bottom: 24px;
  }
  .person-name {
    font-family: "Montserrat", sans-serif;
    font-weight: 800; font-size: 19px; text-transform: uppercase;
  }
  .person-role { font-size: 16px; margin-top: 2px; }
  .person-email { font-size: 15px; font-style: italic; margin-top: 4px; }
  .phones { margin-top: 20px; font-size: 18px; line-height: 1.25; }
  .phone { display: flex; align-items: center; gap: 8px; }
  .phone svg { width: 15px; height: 15px; }
  .address { margin-top: 16px; font-size: 18px; line-height: 1.25; }
</style>
</head>
<body>

  <section class="card card-front">
    <div class="brand">
      <span class="brand-mark"></span>
      <span class="brand-name">HARLOW GRADING LLC</span>
    </div>

    <div class="services-band">
      <svg width="620" height="34" viewBox="0 0 620 34" aria-hidden="true">
        <rect x="70" y="0" width="480" height="34" fill="var(--grey)"/>
        <g fill="var(--grey)">
          <polygon points="6,34 16,0 24,0 14,34"/>
          <polygon points="22,34 32,0 40,0 30,34"/>
          <polygon points="38,34 48,0 56,0 46,34"/>
          <polygon points="54,34 64,0 66,0 66,34"/>
          <polygon points="556,34 566,0 574,0 564,34"/>
          <polygon points="572,34 582,0 590,0 580,34"/>
          <polygon points="588,34 598,0 606,0 596,34"/>
          <polygon points="604,34 614,0 620,0 620,8 612,34"/>
        </g>
      </svg>
      <p class="services-list">
        Driveways<span class="sep">|</span>Site prep<span class="sep">|</span>Retaining walls<span class="sep">|</span>Septic systems<span class="sep">|</span>Rock delivery
      </p>
    </div>
  </section>

  <section class="card card-back">
    <div class="machine-art" role="img" aria-label="Embossed excavator bucket and arm illustration"></div>

    <div class="contact">
      <p class="back-brand">HARLOW</p>
      <p class="person-name">Dale Mercer</p>
      <p class="person-role">Managing Director</p>
      <p class="person-email">E: harlowgradingllc@mailverde.net</p>

      <div class="phones">
        <p class="phone">
          <svg viewBox="0 0 16 16" aria-hidden="true"><rect x="4" y="1" width="8" height="14" rx="1.5" fill="none" stroke="var(--white)" stroke-width="1.4"/><line x1="7" y1="12.5" x2="9" y2="12.5" stroke="var(--white)" stroke-width="1.4"/></svg>
          208-471-9360
        </p>
        <p class="phone">
          <svg viewBox="0 0 16 16" aria-hidden="true"><path d="M4 2 L6.5 5 L5 6.5 C6 8.5 7.5 10 9.5 11 L11 9.5 L14 12 L12.5 14 C7 13.5 2.5 9 2 3.5 Z" fill="none" stroke="var(--white)" stroke-width="1.3" stroke-linejoin="round"/></svg>
          208-396-4815
        </p>
      </div>

      <p class="address">421, Address line<br>goes here, 45452<br>Country Name</p>
    </div>
  </section>

</body>
</html>
```